Prayer Service 12.28.2013

I need a flyer designed for a Christian prayer service. The title and theme is:
"Total and Complete Surrender for Total and Complete Deliverance!"
1. You have creative freedom with imagery and typography
2. I need a quick turnaround time
FLYER DETAILS:
A prayer, anointing, and deliverance all night prayer service, at Brookhaven Assembly.
Saturday December 28 2013 from 9pm-6am.
Special guest speakers, prayer,anointing,and deliverance sessions.
For more information contact Sis Mirela Thornbury at Brookhaven Assembly 347 562 1094 Ext. 4816 or Janelle Corbin at 631 538-2904

```html
<!DOCTYPE html>
<html lang="en">
<head>
<meta charset="utf-8">
<title>Total and Complete Surrender – All Night Prayer Service</title>
<link rel="stylesheet" href="https://fonts.googleapis.com/css2?family=Cinzel:wght@600;700&display=swap">
<style>
  :root {
    --gold-light: #d9a94a;
    --gold-mid: #a86b1f;
    --gold-deep: #5e3510;
    --panel: rgba(62, 52, 42, 0.88);
    --panel-edge: rgba(255, 255, 255, 0.18);
    --cream: #fbf6ec;
    --band: #ffffff;
    --band-text: #5a3a1a;
  }
  * { margin: 0; padding: 0; box-sizing: border-box; }
  html, body { width: 928px; height: 1200px; overflow: hidden; background: #2a1a0c; }
  .flyer {
    position: relative;
    width: 928px;
    height: 1200px;
    overflow: hidden;
    font-family: "Cinzel", "Trajan Pro", serif;
    color: var(--cream);
  }
  .backdrop {
    position: absolute; inset: 0;
    background:
      radial-gradient(ellipse at 85% 20%, rgba(255, 214, 120, 0.55), transparent 45%),
      radial-gradient(ellipse at 10% 70%, rgba(255, 200, 100, 0.35), transparent 50%),
      linear-gradient(135deg, var(--gold-mid) 0%, var(--gold-light) 35%, var(--gold-mid) 60%, var(--gold-deep) 100%);
  }
  .panel {
    position: absolute;
    left: 46px; width: 820px;
    background: var(--panel);
    border: 1px solid var(--panel-edge);
    text-align: center;
    text-shadow: 0 2px 4px rgba(0, 0, 0, 0.6);
  }
  .panel--headline { top: 50px; height: 444px; }
  .panel--details { top: 640px; height: 500px; }
  .date {
    font-weight: 700;
    font-size: 27px;
    letter-spacing: 0.5px;
    padding-top: 20px;
  }
  .rule {
    height: 1px;
    background: rgba(255, 255, 255, 0.55);
  }
  .rule--date { margin: 16px 0 0; }
  .title { margin-top: 98px; font-weight: 700; line-height: 1; }
  .title span { display: block; }
  .title .lead { font-size: 40px; margin-left: -70px; }
  .title .surrender { font-size: 64px; margin-top: 4px; }
  .title .bridge { font-size: 31px; margin-top: 6px; margin-left: 20px; }
  .title .deliverance { font-size: 70px; margin-top: 4px; margin-left: -80px; }
  .band {
    position: absolute;
    left: 0; right: 0; top: 498px; height: 126px;
    background: var(--band);
    border-top: 4px solid var(--band);
    box-shadow: 0 -6px 0 -2px rgba(255,255,255,0.8);
    color: var(--band-text);
    text-align: center;
    font-weight: 700;
    font-size: 26px;
    line-height: 36px;
    padding-top: 14px;
  }
  .sessions {
    font-weight: 700;
    font-size: 27px;
    line-height: 38px;
    margin-top: 102px;
  }
  .rule--contact { width: 608px; margin: 106px auto 0; }
  .contact {
    font-weight: 700;
    font-size: 26px;
    line-height: 37px;
    margin-top: 12px;
  }
</style>
</head>
<body>
  <main class="flyer">
    <div class="backdrop" role="img" aria-label="Golden grunge texture with ornate damask flourishes"></div>

    <section class="panel panel--headline" role="group" aria-label="Event title">
      <p class="date">Saturday, December 28 2013 from 9pm-6am.</p>
      <div class="rule rule--date"></div>
      <h1 class="title">
        <span class="lead">Total and Complete</span>
        <span class="surrender">Surrender</span>
        <span class="bridge">for Total and Complete</span>
        <span class="deliverance">Deliverance!</span>
      </h1>
    </section>

    <section class="band">
      <p>A prayer, anointing and deliverance<br>all night prayer service,<br>at Brookhaven Assembly.</p>
    </section>

    <section class="panel panel--details">
      <p class="sessions">Special guest speakers, prayer, anointing<br>and deliverance sessions.</p>
      <div class="rule rule--contact"></div>
      <p class="contact">
        For more information<br>
        contact Sis Mirela Thornbury<br>
        at Brookhaven Assembly<br>
        347 562 1094 Ext. 4816<br>
        or Janelle Corbin at 631 538-2904
      </p>
    </section>
  </main>
</body>
</html>
```